Peanut Butter for Dogs - Label

Dear Designers,

Our company develops natural & innovative products aimed at enhancing animal (cat & dog) well-being. The company focuses on producing high-end, ethically sourced products that naturally soothe pets, improving their quality of life.

We are currently developing a new CBD-enriched Peanut Butter product for dogs, and we are looking for some label designs that follow our brand image & brand identity.

-> Please see full brief PDF file attached.

Target Market(s)

European Market (French Speaking)

Industry/Entity Type

Pet Food

Font styles to use
Other font styles liked:
• Please see brand kit in PDF brief

Colors

Designer to choose colors to be used in the design.

Requirements
Must have
• Please see brief PDF file attached
Nice to have
Should not have

```html
<!DOCTYPE html>
<html lang="fr">
<head>
<meta charset="utf-8">
<title>Étiquette beurre de cacahuète – VERDALIS</title>
<link href="https://fonts.googleapis.com/css2?family=Poppins:wght@400;500;600;700&display=swap" rel="stylesheet">
<style>
  :root{
    --green:#3a9a7e;
    --ink:#1c1c1c;
    --text:#2a2a2a;
    --paper:#ffffff;
    --page:#f3f4f3;
    --photo-a:#e4e4e2;
    --photo-b:#c9c4bd;
  }
  *{margin:0;padding:0;box-sizing:border-box}
  html,body{width:1200px;height:848px;overflow:hidden;background:var(--page);font-family:"Poppins",sans-serif;color:var(--text)}
  .label{position:absolute;left:30px;top:272px;width:1140px;height:305px;background:var(--paper);overflow:hidden}
  .abs{position:absolute}
  .band{left:0;top:0}
  .heading{color:var(--green);font-weight:600;font-size:16px;letter-spacing:-.2px;line-height:1}
  .intro-title{left:54px;top:30px}
  .intro-text{left:31px;top:60px;width:300px;font-size:13.5px;line-height:18.2px}
  .usage{left:20px;top:166px;width:324px;height:103px;border:2px dashed var(--green)}
  .usage .heading{text-align:center;margin-top:9px}
  .usage p{font-size:13.2px;line-height:14.6px;padding:4px 10px 0 11px}
  .brand{left:476px;top:66px;width:200px;text-align:center;font-weight:500;font-size:17px;color:var(--ink);letter-spacing:.5px}
  .brand .dot{display:inline-block;width:8px;height:8px;border-radius:50%;background:var(--green);margin-right:6px;vertical-align:2px}
  .title{left:389px;top:114px;width:206px}
  .title .name{font-size:37px;font-weight:700;color:var(--green);line-height:1;letter-spacing:-.5px}
  .title .sub{font-size:21px;font-weight:700;color:var(--ink);line-height:1;margin-top:2px;padding-left:2px}
  .title .rule{height:2px;background:var(--green);margin:6px 0 4px 3px}
  .title .dose{font-size:18px;font-weight:600;color:var(--ink);line-height:1;padding-left:2px}
  .title .dose span{color:var(--green)}
  .title .product{font-size:16.5px;font-weight:600;color:var(--green);line-height:1;padding-left:3px}
  .photo{left:600px;top:108px}
  .badge{left:703px;top:18px}
  .dosage-title{left:846px;top:30px;width:260px;text-align:center}
  .dosage{left:846px;top:49px;border-collapse:separate;border-spacing:5px 4px;margin:-4px -5px}
  .dosage td{background:var(--green);color:#fff;height:24px;font-size:14.5px;line-height:1}
  .dosage .size{width:64px;text-align:center;font-weight:500}
  .dosage .amount{width:190px;text-align:center;font-weight:600}
  .tip-title{left:846px;top:136px;width:250px;text-align:center}
  .tip-text{left:846px;top:152px;width:270px;font-size:13.2px;line-height:14.8px}
  .divider{left:846px;top:209px;width:294px;border-top:2px dashed var(--green)}
  .ing-title{left:846px;top:224px;width:250px;text-align:center}
  .ing-text{left:846px;top:240px;width:285px;font-size:13.2px;line-height:14.8px}
  .ing-text .accent{color:var(--green)}
</style>
</head>
<body>
<main class="label">
  <svg class="abs band" width="1140" height="45" viewBox="0 0 1140 45" aria-hidden="true">
    <path d="M0 0 H1140 V11 H612 Q588 12 576 40 Q564 12 540 11 H0 Z" fill="var(--green)"/>
  </svg>

  <h2 class="abs heading intro-title">DOUX COMME UNE CARESSE</h2>
  <p class="abs intro-text">Enrichi en extrait de chanvre naturellement apaisant, le beurre de cacahuète VERDANUTSTM est une délicieuse friandise d’occupation à lécher.</p>

  <section class="abs usage">
    <h2 class="heading">UTILISATION</h2>
    <p>Laissez votre chien lécher cette gourmandise pour traverser en douceur les événements stressants du quotidien (absence, toilettage, trajet en voiture, etc.)</p>
  </section>

  <div class="abs brand"><span class="dot"></span>VERDALIS</div>

  <div class="abs title">
    <div class="name">TENDRAL</div>
    <div class="sub">RÉCONFORTANTE</div>
    <div class="rule"></div>
    <div class="dose"><span>CBD</span> 150 MG</div>
    <div class="rule"></div>
    <div class="product">BEURRE DE CACAHUÈTE</div>
  </div>

  <svg class="abs photo" width="230" height="200" viewBox="0 0 230 200">
    <circle cx="112" cy="112" r="111" fill="var(--green)"/>
    <defs>
      <linearGradient id="photoTone" x1="0" y1="0" x2="1" y2="1">
        <stop offset="0" stop-color="var(--photo-a)"/>
        <stop offset="1" stop-color="var(--photo-b)"/>
      </linearGradient>
    </defs>
    <circle cx="106" cy="119" r="104" fill="url(#photoTone)" role="img" aria-label="Photo d’un chien shar-pei clair léchant sa truffe"/>
  </svg>

  <svg class="abs badge" width="94" height="94" viewBox="0 0 94 94" role="img" aria-label="À lécher, 100 % naturel, anti-stress">
    <circle cx="47" cy="47" r="44" fill="#fff" stroke="var(--green)" stroke-width="1.6"/>
    <circle cx="47" cy="47" r="26" fill="none" stroke="var(--green)" stroke-width="1.4"/>
    <defs>
      <path id="arcTop" d="M17 47 A30 30 0 0 1 77 47"/>
      <path id="arcBottom" d="M14 50 A33 33 0 0 0 80 50"/>
    </defs>
    <text font-family="Poppins, sans-serif" font-size="11" font-weight="500" fill="var(--green)"><textPath href="#arcTop" startOffset="50%" text-anchor="middle">À lécher</textPath></text>
    <text font-family="Poppins, sans-serif" font-size="11" font-weight="500" fill="var(--green)"><textPath href="#arcBottom" startOffset="50%" text-anchor="middle" dominant-baseline="hanging">Anti-Stress</textPath></text>
    <text x="47" y="49" text-anchor="middle" font-family="Poppins, sans-serif" font-size="16" font-weight="600" fill="var(--green)">100%</text>
    <text x="47" y="60" text-anchor="middle" font-family="Poppins, sans-serif" font-size="8.5" font-weight="600" fill="var(--green)">NATUREL</text>
  </svg>

  <h2 class="abs heading dosage-title">DOSAGE TABLE</h2>
  <table class="abs dosage">
    <tr><td class="size">PETIT</td><td class="amount">1 Cuillère à café</td></tr>
    <tr><td class="size">MOYEN</td><td class="amount">1 Cuillère à café</td></tr>
    <tr><td class="size">GRAND</td><td class="amount">1 Cuillère à café</td></tr>
  </table>

  <h2 class="abs heading tip-title">ASTUCE</h2>
  <p class="abs tip-text">Pour une utilisation optimale, étalez le beurre de cacahuète<br>sur le tapis de léchage VERDALICKTM.</p>

  <div class="abs divider"></div>

  <h2 class="abs heading ing-title">INGRÉDIENTS</h2>
  <p class="abs ing-text">Beurre de cacahuète, extrait de chanvre (0% THC).<br><span class="accent">Poids Net</span> : 250g</p>
</main>
</body>
</html>
```